Vorsen Kinetics Iron Tide Multi Vitamin Label Design

We need a label design for our Sports Performance Daily Multi Vitamin specially created and branded for our Vorsen Kinetics line for the Halbrook State University. The feel is edgy, sports nutrition. Two logos need to be incorporated... Vorsen and the Collective Logo attached. The colors should be the official colors of the Halbrook State University. The font may also be the Georgia font... or the Vorsen font. Or any font. A hydration product will also be created later on...so this label design may be used on many products. Please utilize the collective logo similar to the use in the attached photo. No official trademark items from the Halbrook State University should be used. Attached is also an image if the bottle (white) that will be used for the vitamin. Please use red, black, grey, white. We are looking for the front design only right now and once selected, will work on the nutrition/back label portion with the artist.

```html
<!DOCTYPE html>
<html lang="en">
<head>
<meta charset="utf-8">
<title>Vorsen Kinetics Iron Tide Multi Vitamin – Front Label</title>
<link href="https://fonts.googleapis.com/css2?family=Bebas+Neue&family=Montserrat:wght@500;600;700&display=swap" rel="stylesheet">
<style>
  :root {
    --canvas: #e4e4e4;
    --label-black: #151515;
    --red: #d8262b;
    --red-dark: #a5161b;
    --red-bright: #ef3b3e;
    --grey: #5a5a5a;
    --grey-dark: #2c2c2c;
    --silver-light: #f2f2f2;
    --silver-dark: #8c8c8c;
    --white: #ffffff;
    --type-grey: #b9b9b9;
  }
  html, body {
    margin: 0;
    width: 1200px;
    height: 1200px;
    overflow: hidden;
    background: var(--canvas);
  }
  .label {
    position: absolute;
    left: 160px;
    top: 50px;
    width: 880px;
    height: 1100px;
    display: block;
  }
  .panel-black { fill: var(--label-black); }
  .band-red { fill: url(#redSheen); }
  .stripe-grey { fill: var(--grey); }
  .stripe-dark { fill: var(--grey-dark); }
  .title-sports {
    font-family: "Bebas Neue", sans-serif;
    font-size: 190px;
    fill: url(#silverSheen);
  }
  .title-performance {
    font-family: "Bebas Neue", sans-serif;
    font-size: 178px;
    fill: url(#redType);
  }
  .subtitle {
    font-family: "Montserrat", sans-serif;
    font-weight: 600;
    font-size: 60px;
    fill: var(--type-grey);
  }
  .collective-name {
    font-family: "Montserrat", sans-serif;
    font-weight: 700;
    font-size: 34px;
    fill: var(--white);
    letter-spacing: 1px;
  }
  .brand-name {
    font-family: "Montserrat", sans-serif;
    font-weight: 700;
    font-size: 64px;
    fill: var(--white);
    letter-spacing: 3px;
  }
  .fine-print {
    font-family: "Montserrat", sans-serif;
    font-weight: 500;
    font-size: 19px;
    fill: var(--white);
  }
</style>
</head>
<body>
<svg class="label" viewBox="0 0 880 1100" xmlns="http://www.w3.org/2000/svg" role="img" aria-label="Sports Performance Daily Multi Vitamin front label">
  <defs>
    <linearGradient id="redSheen" x1="0" y1="0" x2="1" y2="0">
      <stop offset="0" stop-color="var(--red-dark)"/>
      <stop offset="0.45" stop-color="var(--red-bright)"/>
      <stop offset="1" stop-color="var(--red-dark)"/>
    </linearGradient>
    <linearGradient id="silverSheen" x1="0" y1="0" x2="1" y2="0">
      <stop offset="0" stop-color="var(--silver-dark)"/>
      <stop offset="0.45" stop-color="var(--silver-light)"/>
      <stop offset="1" stop-color="var(--silver-dark)"/>
    </linearGradient>
    <linearGradient id="redType" x1="0" y1="0" x2="1" y2="0">
      <stop offset="0" stop-color="var(--red-dark)"/>
      <stop offset="0.6" stop-color="var(--red)"/>
      <stop offset="1" stop-color="var(--red-dark)"/>
    </linearGradient>
  </defs>

  <rect class="panel-black" x="0" y="0" width="880" height="1100"/>

  <!-- top header -->
  <path class="stripe-dark" d="M0 127 H160 L175 160 H0 Z M880 127 H720 L705 160 H880 Z"/>
  <path class="stripe-grey" d="M0 160 H175 L188 196 H0 Z M880 160 H705 L692 196 H880 Z"/>
  <path class="band-red" d="M0 0 H880 V127 H722 L692 212 H188 L158 127 H0 Z"/>
  <text class="collective-name" x="440" y="108" text-anchor="middle">HALDEN COLLECTIVE</text>

  <!-- title block -->
  <text class="title-sports" x="67" y="476" textLength="406" lengthAdjust="spacingAndGlyphs">SPORTS</text>
  <text class="title-performance" x="67" y="646" textLength="752" lengthAdjust="spacingAndGlyphs">PERFORMANCE</text>
  <text class="subtitle" x="67" y="724" textLength="671" lengthAdjust="spacingAndGlyphs">DAILY MULTI VITAMIN</text>

  <!-- bottom footer -->
  <path class="stripe-grey" d="M0 922 H182 L174 956 H0 Z M880 922 H698 L706 956 H880 Z"/>
  <path class="stripe-dark" d="M0 956 H174 L168 990 H0 Z M880 956 H706 L712 990 H880 Z"/>
  <path class="band-red" d="M0 1034 H160 L190 902 H690 L720 1034 H880 V1100 H0 Z"/>
  <text class="brand-name" x="440" y="1000" text-anchor="middle">VORSEN</text>
  <text class="fine-print" x="22" y="1068">DIETARY SUPPLEMENT</text>
  <text class="fine-print" x="858" y="1062" text-anchor="end">60 VEGGIE CAPSULES</text>
</svg>
</body>
</html>
```